Label designs for three different cider varieties

The Larkmoor Perry Works is a family run business. We have been making cider within the family as a hobby for over 100 years and we have recently decided to start to try to sell the cider. Therefore this project is to create a logo and three product labels for three different varieties of cider. So we should end up with four files; one for the logo and one for each of the labels. The files need to be in an editable format for us so that we can add edit the batch numbers e.g. PNG file.
For the logo we would like to use the Pellow Family Shield since Pellow is our family name. We would like it adapted into a cider themed crest, for example with apples and trees. We are open to ideas about the logo but this is just our initial idea. Example of the original Pellow Family Shield can be seen in the link below:
http://www.vinshadeheraldry.net/arms/Pellow-England.jpg
The labels should be no bigger than 93mm in height and 213mm in length. Each label should be similar in style so it is clear the three different varieties of cider are from the same company. Each label must have the following information since this is a legal requirement:
- The logo you have created
- The Larkmoor Perry Works Ltd.
- 52 Mirefield Row, Taunton, Somerset, TA4 9QX
- Alcohol: 6% vol
- 500ml
- Allergens: Contains Sulphites for freshness
- There needs to be space on the label for batch numbers. This is four numbers e.g. 1701.
- Family craft cider makers using only premium apples from our own traditional Somerset orchard.
The names of the three cider varieties are:
- Larkmoor Heritage
- Larkmoor Amber
- Larkmoor Kingsbury
Our initial idea is that each variety would have its own colour associated with it; i.e. black themed label for Larkmoor Heritage, gold themed label for Larkmoor Amber and a red themed label for Larkmoor Kingsbury. The crest logo you have created would then be in the themed colour for that cider variety i.e. black, gold or red.
We would like the labels to reflect the following themes for our brand:
- High end premium brand
- Clean and simple design
- Modern
Overall we are very open to ideas and we do not want to constrain your creativity. All of the above is just our initial ideas but we would love to see what ideas you have. The only things that cannot change are what must be on the label since this is a legal requirement we have to meet.

```html
<!DOCTYPE html>
<html lang="en">
<head>
<meta charset="utf-8">
<title>Larkmoor Kingsbury – Cider Label</title>
<link href="https://fonts.googleapis.com/css2?family=Montserrat:wght@300;400&family=Sorts+Mill+Goudy&family=Great+Vibes&family=Oswald:wght@400&display=swap" rel="stylesheet">
<style>
  :root {
    --backdrop: #5b5b5b;
    --paper: #ffffff;
    --ink: #1a1a1a;
    --accent-red: #e3202a;
    --art-light: #e9d6d6;
    --art-mid: #d9b5b6;
  }
  * { margin: 0; padding: 0; box-sizing: border-box; }
  html, body { width: 1200px; height: 1200px; overflow: hidden; }
  body { background: var(--backdrop); position: relative; font-family: "Montserrat", sans-serif; color: var(--ink); }

  .label {
    position: absolute; left: 352px; top: 27px; width: 461px; height: 1055px;
    background: var(--paper); border: 1px solid #000;
  }
  .label > * { position: absolute; }

  .abv { left: 26px; top: 36px; font-size: 20px; font-weight: 300; line-height: 23px; text-align: center; }
  .volume { right: 32px; top: 48px; font-size: 20px; font-weight: 300; }

  .maker-mark { left: 178px; top: 24px; width: 104px; display: flex; flex-direction: column; align-items: center; gap: 10px; }
  .maker-mark .mark-dot { width: 72px; height: 72px; border-radius: 50%; background: var(--accent-red); }
  .maker-mark .mark-name { font-family: "Sorts Mill Goudy", serif; font-size: 22px; line-height: 1; color: var(--ink); }

  .tagline {
    left: 0; width: 100%; top: 184px; text-align: center;
    font-family: "Sorts Mill Goudy", serif; font-size: 22.5px; line-height: 27.5px;
  }

  .variety { left: 60px; top: 328px; width: 360px; height: 175px; }
  .variety .variety-pre { position: absolute; right: 100px; top: 12px; font-family: "Great Vibes", cursive; font-size: 52px; line-height: 1; }
  .variety .variety-name { position: absolute; left: 0; top: 50px; font-family: "Great Vibes", cursive; font-size: 96px; line-height: 1; white-space: nowrap; }
  .variety .variety-sub { position: absolute; right: 72px; top: 152px; font-family: "Oswald", sans-serif; font-size: 20px; letter-spacing: 7px; line-height: 1; }

  .apple-art {
    left: 131px; top: 510px; width: 201px; height: 221px;
    background: linear-gradient(180deg, var(--art-light), var(--art-mid));
  }

  .legal {
    left: 0; width: 100%; top: 815px; text-align: center;
    font-size: 20px; font-weight: 300; line-height: 22.5px; letter-spacing: 0.2px;
  }

  .band-red { left: 0; top: 947px; width: 100%; height: 12px; background: var(--accent-red); }
  .band-black { left: 0; top: 963px; width: 100%; height: 6px; background: #000; }

  .batch { left: 0; width: 100%; top: 978px; text-align: center; font-size: 52px; font-weight: 300; color: var(--accent-red); line-height: 60px; }
</style>
</head>
<body>
  <main class="label">
    <p class="abv">Alcohol:<br>6% vol</p>

    <div class="maker-mark">
      <span class="mark-dot"></span>
      <span class="mark-name">Pellow</span>
    </div>

    <p class="volume">500ml</p>

    <p class="tagline">Family craft cider makers using<br>only premium apples from our<br>own traditional Somerset orchard.</p>

    <div class="variety">
      <span class="variety-pre">The</span>
      <span class="variety-name">Larkmoor</span>
      <span class="variety-sub">KINGSBURY</span>
    </div>

    <div class="apple-art" role="img" aria-label="Illustration area: red apple with a green leaf"></div>

    <p class="legal">The Larkmoor Perry Works Ltd.<br>52 Mirefield Row,<br>Taunton, Somerset, TA4 9QX<br>Allergens:<br>Contains Sulphites for freshness</p>

    <div class="band-red"></div>
    <div class="band-black"></div>

    <p class="batch">1703</p>
  </main>
</body>
</html>
```